Corporate Two Sided Business Card

Looking for a Corporate "edgy" Modern look and feel for a business card

We are looking at two options. Dark background with our logo on it, white background with our logo on it - The background is more - Charcoal / Graphite then black

Details will be

Danielle Forsk

Licensee / Director

m. 0428 519 064

e. danielle@quorvela.com.au

quorvela.com.au

Target Market(s)

Professional Business people that refer use business and clients that own Investment Properties

Industry/Entity Type

Business

Contact Information for Business Card

Details will be

Danielle Forsk

Licensee / Director

m. 0428 519 064

quorvela.com.au

Font styles to use
Serif

Colors
000000
ec1f27
eeeeee
ffffff

Requirements
Must have
• Two options - White Background and Dark Background. - Two sided
Nice to have
• A design that is edgy, modern and new to look instead of boring style corporate cards - It should be a full integrated design
Should not have
• Block looking - Cheap.

```html
<!DOCTYPE html>
<html lang="en">
<head>
<meta charset="utf-8">
<title>Quorvela — Business Card</title>
<link href="https://fonts.googleapis.com/css2?family=Montserrat:wght@500&family=Open+Sans:wght@400;600&display=swap" rel="stylesheet">
<style>
  :root {
    --backdrop: #232323;
    --card: #141414;
    --red: #ec1f27;
    --light: #eeeeee;
    --white: #ffffff;
    --muted: #b9b9b9;
  }
  * { margin: 0; padding: 0; box-sizing: border-box; }
  html, body {
    width: 1200px;
    height: 1017px;
    overflow: hidden;
    background: var(--backdrop);
  }
  .canvas {
    position: relative;
    width: 1200px;
    height: 1017px;
    background: radial-gradient(ellipse at 50% 40%, #2b2b2b 0%, var(--backdrop) 70%);
  }
  .card {
    position: absolute;
    width: 520px;
    height: 318px;
    background: var(--card);
    border-radius: 3px;
    box-shadow: 0 18px 40px rgba(0, 0, 0, 0.45);
    display: flex;
    align-items: center;
    justify-content: center;
  }
  .card--front { left: 90px; top: 150px; }
  .card--back  { left: 590px; top: 540px; }

  .brand {
    display: flex;
    align-items: center;
    gap: 14px;
  }
  .brand__mark {
    width: 22px;
    height: 22px;
    background: var(--red);
  }
  .brand__name {
    font-family: "Montserrat", sans-serif;
    font-weight: 500;
    font-size: 54px;
    letter-spacing: 1px;
    color: var(--white);
    line-height: 1;
  }

  .contact {
    text-align: center;
    font-family: "Open Sans", sans-serif;
    color: var(--light);
  }
  .contact__name {
    font-weight: 600;
    font-size: 15px;
    letter-spacing: 0.5px;
    text-transform: uppercase;
    color: var(--red);
  }
  .contact__role {
    font-size: 15px;
    letter-spacing: 0.5px;
    text-transform: uppercase;
    color: var(--white);
    margin-top: 2px;
  }
  .contact__rule {
    width: 46px;
    height: 1px;
    background: var(--red);
    margin: 9px auto;
  }
  .contact__line {
    font-size: 14px;
    line-height: 1.45;
    color: var(--muted);
  }
</style>
</head>
<body>
  <main class="canvas">
    <section class="card card--front" aria-label="Card front">
      <div class="brand">
        <span class="brand__mark" aria-hidden="true"></span>
        <span class="brand__name">quorvela</span>
      </div>
    </section>

    <section class="card card--back" aria-label="Card back">
      <div class="contact">
        <p class="contact__name">Danielle Forsk</p>
        <p class="contact__role">Licensee / Director</p>
        <div class="contact__rule"></div>
        <p class="contact__line">M : 0428 519 064</p>
        <p class="contact__line">danielle@quorvela.com.au</p>
        <div class="contact__rule"></div>
        <p class="contact__line">www.quorvela.com.au</p>
      </div>
    </section>
  </main>
</body>
</html>
```